professional health club Info Flyer

we need a professional health club DL flyer that will provide information regarding our 24/7 health club services to enquiries whilst we are unstaffed. these will be placed outside on main street.

www.vitrova.club

On the reverse side, we want to offer 2 introductory specials;
1. free 7 day trial
2. Membership, classes & personal training introductory month3 personal training sessions and month 24/7 membership and classes for $99.95 (saving of over $159.85)
conditions: valid for new members only

SIZE: DL with double sided

Target Market(s)

professional, male and female of all ages (in particular those 30+)

Industry/Entity Type

Health And Wellness

Colors
33a6d7
abd037
f78f20
ffffff

Requirements
Must have
• - professional allied health feel about flyer with images
• - contact details
• - services provided include 24/7 memberships, classes, special population group training, Exercise physiology, physiotherapy, massage, nutrition, rehabilitation.
• - a catch to get them to contact us
• - our slogan "We are here to improve your quality of life"

```html
<!DOCTYPE html>
<html lang="en">
<head>
<meta charset="utf-8">
<title>Vitrova Health Club – DL Flyer</title>
<link href="https://fonts.googleapis.com/css2?family=Roboto+Condensed:ital,wght@0,300;0,400;0,700;1,700&family=Roboto:ital,wght@0,400;0,700;1,800&display=swap" rel="stylesheet">
<style>
  :root{
    --sky:#33a6d7;
    --lime:#abd037;
    --green:#6cb52d;
    --orange:#f78f20;
    --orange-deep:#ec5a13;
    --royal:#1f5fb0;
    --navy:#17337f;
    --ink:#2b2b3a;
    --white:#ffffff;
    --paper:#f3f4f6;
    --stage:#e4e5e7;
  }
  *{box-sizing:border-box;margin:0;padding:0}
  html,body{width:1200px;height:1200px;overflow:hidden;background:var(--stage)}
  body{font-family:"Roboto Condensed",sans-serif;color:var(--ink);position:relative}

  .flyer{position:absolute;top:110px;width:440px;height:980px;background:linear-gradient(180deg,var(--white),var(--paper) 45%,var(--white));box-shadow:0 6px 22px rgba(0,0,0,.18);overflow:hidden}
  .flyer--front{left:150px}
  .flyer--back{left:610px;background:var(--white)}

  /* brand */
  .brand{position:absolute;left:0;right:0;display:flex;align-items:center;justify-content:center;gap:14px}
  .brand__mark{width:56px;height:56px;border-radius:50%;background:var(--royal)}
  .brand__text{display:flex;flex-direction:column;align-items:flex-start}
  .brand__name{font-weight:700;font-size:50px;line-height:1;color:var(--navy);letter-spacing:1px}
  .brand__sub{font-size:13px;font-weight:700;color:var(--green);letter-spacing:2px;margin-top:2px}
  .tagline{position:absolute;left:0;right:0;text-align:center;font-family:"Roboto",sans-serif;font-style:italic;font-weight:800;font-size:18px;color:var(--navy)}

  /* front */
  .headline{position:absolute;left:46px;top:168px;line-height:.96}
  .headline span{display:block;white-space:nowrap}
  .headline__l1{font-weight:400;font-size:56px;color:var(--green)}
  .headline__l2{font-weight:700;font-size:50px;color:var(--sky)}
  .headline__l3{font-weight:300;font-size:57px;color:var(--navy)}
  .badge{position:absolute;left:44px;top:345px;width:172px;height:60px;border:2px solid var(--sky);border-radius:14px;background:var(--white);display:flex;align-items:center;gap:6px;padding-left:10px;z-index:2}
  .badge__big{font-weight:700;font-size:38px;color:var(--navy);white-space:nowrap}
  .badge__small{font-size:16px;line-height:1.05;color:var(--navy);white-space:nowrap}
  .badge__small b{font-weight:700}

  .band{position:absolute;left:0;right:0;top:468px;height:282px;background:linear-gradient(180deg,var(--royal),var(--navy));border-top:4px solid var(--orange)}
  .photo-people{position:absolute;left:170px;top:345px;width:270px;height:405px;background:linear-gradient(180deg,#d8dde3,#8d97a5);border-radius:120px 120px 0 0}
  .photo-gym{position:absolute;left:20px;top:518px;width:162px;height:162px;border-radius:50%;border:5px solid var(--white);background:linear-gradient(160deg,#c9d3da,#4c5f6a)}

  .services__tab{position:absolute;left:50%;transform:translateX(-50%);top:740px;background:var(--orange);color:var(--white);font-weight:700;font-size:24px;padding:2px 18px;border-radius:3px 3px 0 0;white-space:nowrap}
  .services{position:absolute;left:14px;right:14px;top:792px;height:100px;border:2px solid var(--orange);border-radius:14px;background:linear-gradient(180deg,var(--white),#ebeced);display:grid;grid-template-columns:1.1fr 1.15fr .9fr;column-gap:6px;padding:14px 8px 0 10px}
  .services ul{list-style:none}
  .services li{font-size:15px;line-height:19px;color:var(--ink);white-space:nowrap}
  .services li::before{content:"• ";color:var(--ink)}

  .url-bar{position:absolute;left:0;right:0;top:925px;height:36px;background:var(--sky);color:var(--white);text-align:center;font-family:"Roboto",sans-serif;font-weight:700;font-size:20px;letter-spacing:4px;line-height:36px}

  /* back */
  .back-photo{position:absolute;left:0;right:0;top:215px;height:345px;background:linear-gradient(160deg,#4b8fd6,#1e5fb5 60%,#274a8a);border-top:4px solid var(--orange)}
  .trial{position:absolute;left:14px;top:470px;width:160px;height:160px;border-radius:50%;background:radial-gradient(circle at 40% 35%,var(--orange),var(--orange-deep));border:5px solid var(--white);box-shadow:0 3px 8px rgba(0,0,0,.25);color:var(--white);text-align:center;padding-top:26px}
  .trial__free{display:block;font-weight:700;font-style:italic;font-size:58px;line-height:1}
  .trial__days{display:block;font-weight:700;font-size:25px;line-height:1.1;white-space:nowrap}
  .valid{position:absolute;left:186px;top:576px}
  .valid__lead{display:block;font-weight:700;font-size:34px;color:var(--navy);line-height:1}
  .valid__rest{display:block;font-size:26px;color:var(--ink);line-height:1.2;white-space:nowrap}

  .offer-list{position:absolute;left:18px;top:650px;list-style:none;font-size:15px;line-height:18px;color:var(--ink)}
  .offer-list li::before{content:"• "}
  .offer-detail{position:absolute;left:150px;top:664px;width:270px;font-size:15px;line-height:18px;color:var(--ink)}
  .offer-detail::before{content:"• "}
  .price-pill{position:absolute;left:-10px;top:728px;width:445px;height:34px;background:var(--orange-deep);border-radius:0 17px 17px 0;color:var(--white);font-weight:700;font-size:18.5px;line-height:34px;padding-left:20px;white-space:nowrap}

  .contact__tab{position:absolute;left:150px;top:776px;background:var(--green);color:var(--white);font-weight:700;font-size:23px;padding:2px 14px;white-space:nowrap}
  .contact{position:absolute;left:120px;top:816px;width:215px;font-size:14.5px;line-height:17px;color:var(--ink)}
  .contact__name{font-size:22px;line-height:24px;color:var(--royal);margin-bottom:2px}
  .contact__row{display:flex;gap:5px;align-items:flex-start;white-space:nowrap}
  .contact__row svg{flex:0 0 11px;margin-top:3px}
  .photo-round{position:absolute;border-radius:50%;border:4px solid var(--sky)}
  .photo-round--left{left:-30px;top:782px;width:96px;height:96px;background:linear-gradient(150deg,#d9e9f2,#7fb2cf)}
  .photo-round--right{left:335px;top:808px;width:96px;height:96px;background:linear-gradient(150deg,#f1f3f5,#9aa9b5)}
</style>
</head>
<body>

<section class="flyer flyer--front" aria-label="Flyer front">
  <div class="brand" style="top:30px">
    <span class="brand__mark" aria-hidden="true"></span>
    <div class="brand__text">
      <span class="brand__name">Vitrova</span>
      <span class="brand__sub">HEALTH CLUB</span>
    </div>
  </div>
  <p class="tagline" style="top:124px">Improving your quality of life</p>

  <h1 class="headline">
    <span class="headline__l1">WE ARE HERE</span>
    <span class="headline__l2">TO IMPROVE YOUR</span>
    <span class="headline__l3">QUALITY OF LIFE</span>
  </h1>

  <div class="band"></div>
  <div class="photo-people" role="img" aria-label="Photo of a man and a woman training with a dumbbell"></div>
  <div class="photo-gym" role="img" aria-label="Photo of the gym floor with training machines"></div>

  <div class="badge">
    <span class="badge__big">24/7</span>
    <span class="badge__small">Health club<br><b>services</b></span>
  </div>

  <div class="services__tab">Services Provided</div>
  <div class="services">
    <ul><li>24/7 memberships</li><li>Classes</li><li>Special Population</li></ul>
    <ul><li>Group training</li><li>Exercise physiology</li><li>Physiotherapy</li></ul>
    <ul><li>Massage</li><li>Nutrition</li><li>Rehabilitation.</li></ul>
  </div>

  <div class="url-bar">www.vitrova.club</div>
</section>

<section class="flyer flyer--back" aria-label="Flyer reverse">
  <div class="brand" style="top:52px">
    <span class="brand__mark" aria-hidden="true"></span>
    <div class="brand__text">
      <span class="brand__name">Vitrova</span>
      <span class="brand__sub">HEALTH CLUB</span>
    </div>
  </div>
  <p class="tagline" style="top:146px">Improving your quality of life</p>

  <div class="back-photo" role="img" aria-label="Photo of a trainer coaching a woman lifting a dumbbell in a blue gym"></div>

  <div class="trial">
    <span class="trial__free">FREE</span>
    <span class="trial__days">7 DAY TRIAL</span>
  </div>
  <p class="valid">
    <span class="valid__lead">Valid for</span>
    <span class="valid__rest">New Members only</span>
  </p>

  <ul class="offer-list"><li>Membership</li><li>Classes &amp;</li></ul>
  <p class="offer-detail">Personal training introductory month3 personal training sessions and month 24/7 membership</p>
  <div class="price-pill">CLASSES FOR $99.95 (SAVING OF OVER $159.85)</div>

  <div class="photo-round photo-round--left" role="img" aria-label="Photo of a woman stretching"></div>
  <div class="photo-round photo-round--right" role="img" aria-label="Photo of a physiotherapist treating a client"></div>

  <div class="contact__tab">Contact Us</div>
  <address class="contact" style="font-style:normal">
    <div class="contact__name">Dana Whitfield</div>
    <div class="contact__row">
      <svg width="11" height="13" viewBox="0 0 11 13" aria-hidden="true"><path d="M5.5 0A4.5 4.5 0 0 0 1 4.5C1 8 5.5 13 5.5 13S10 8 10 4.5A4.5 4.5 0 0 0 5.5 0Zm0 6.2a1.7 1.7 0 1 1 0-3.4 1.7 1.7 0 0 1 0 3.4Z" fill="#17337f"/></svg>
      <span>57 Harbour View Road,<br>Easthaven NSW 2290</span>
    </div>
    <div class="contact__row">
      <svg width="11" height="9" viewBox="0 0 11 9" aria-hidden="true"><rect x=".5" y=".5" width="10" height="8" fill="none" stroke="#17337f"/><path d="M.5.5 5.5 5l5-4.5" fill="none" stroke="#17337f"/></svg>
      <span>dana@vitrova.club</span>
    </div>
    <div class="contact__row">
      <svg width="11" height="11" viewBox="0 0 11 11" aria-hidden="true"><path d="M2.2 0 4 2.6 2.9 3.8c.6 1.6 2.4 3.4 4.1 4.1l1.2-1.1L11 8.6 9.6 11C4.5 10.6.4 6.5 0 1.4Z" fill="#17337f"/></svg>
      <span>+612 90001234</span>
    </div>
  </address>

  <div class="url-bar">www.vitrova.club</div>
</section>

</body>
</html>
```